KGDB Business Card

Looking for a business card design to incorporate our branding. We want to only use the colors listing in the Branding Package (attached).
Updates

Target Market(s)

People who need their phone or device fixed.

Industry/Entity Type

Electronics

Contact Information for Business Card

Please use:

Bright Circuit Mending Depot LLC
3478 S Ridge Trail 2210 E
Suite 417
San Antonio, TX 78341

Marcus Delwyn, Store Manager

(210) 555-0143

Requirements
Must have
• Must include the colors that are contained within the Branding Package PDF file.

```html
<!DOCTYPE html>
<html lang="en">
<head>
<meta charset="utf-8">
<title>KGDB Business Card</title>
<link rel="stylesheet" href="https://fonts.googleapis.com/css2?family=Arimo:wght@400&display=swap">
<style>
  :root {
    --brand-orange: #f05324;
    --brand-orange-deep: #e84c20;
    --card-white: #ffffff;
    --card-white-shade: #f2f2f2;
    --text-grey: #7a7a7a;
    --text-dark: #333333;
    --backdrop: #5a5a5a;
  }
  * { box-sizing: border-box; margin: 0; padding: 0; }
  html, body {
    width: 1200px;
    height: 1082px;
    overflow: hidden;
  }
  body {
    background: var(--backdrop);
    font-family: "Arimo", Arial, sans-serif;
    position: relative;
  }
  .card {
    position: absolute;
    width: 628px;
    height: 356px;
  }
  .card--front {
    left: 286px;
    top: 180px;
    background: radial-gradient(ellipse at 35% 10%, var(--card-white-shade) 0%, var(--card-white) 60%);
  }
  .card--back {
    left: 289px;
    top: 569px;
    background: radial-gradient(ellipse at 50% 30%, var(--brand-orange) 0%, var(--brand-orange-deep) 100%);
  }
  .brand {
    position: absolute;
    display: flex;
    align-items: center;
    gap: 12px;
    font-size: 22px;
    line-height: 1;
    white-space: nowrap;
  }
  .brand__square {
    width: 38px;
    height: 38px;
    border-radius: 6px;
    flex: none;
  }
  .card--front .brand {
    right: 36px;
    top: 66px;
    color: var(--brand-orange);
  }
  .card--front .brand__square { background: var(--brand-orange); }
  .card--back .brand {
    left: 50%;
    top: 50%;
    transform: translate(-50%, -50%);
    color: var(--card-white);
  }
  .card--back .brand__square { background: var(--card-white); }

  .contact {
    position: absolute;
    left: 37px;
    top: 176px;
  }
  .contact__name {
    font-size: 23px;
    color: var(--brand-orange);
    line-height: 28px;
  }
  .contact__title {
    font-size: 17px;
    color: var(--text-grey);
    line-height: 24px;
  }
  .contact__phone {
    font-size: 16px;
    color: var(--text-dark);
    line-height: 24px;
  }
  .contact__phone-label { color: var(--brand-orange); }
  .contact__address {
    margin-top: 12px;
    font-size: 15px;
    font-style: normal;
    color: var(--text-dark);
    line-height: 23px;
  }
</style>
</head>
<body>
  <section class="card card--front">
    <div class="brand">
      <span class="brand__square"></span>
      <span class="brand__name">Bright Circuit Mending Depot</span>
    </div>
    <div class="contact">
      <p class="contact__name">Marcus Delwyn</p>
      <p class="contact__title">Store Manager</p>
      <p class="contact__phone"><span class="contact__phone-label">Phone:</span> (210) 555-0143</p>
      <address class="contact__address">
        3478 S Ridge Trail 2210 E<br>
        Suite 417<br>
        San Antonio, TX 78341
      </address>
    </div>
  </section>

  <section class="card card--back">
    <div class="brand">
      <span class="brand__square"></span>
      <span class="brand__name">Bright Circuit Mending Depot</span>
    </div>
  </section>
</body>
</html>
```